Lantern Jubilee Flyer

I need an 8.5x11 or 8.5x14 or 11x17 flyer for a benefit concert. Logo has already been designed; uploading several different versions, and you could choose which you want to use. For flyer design: something subtly musical (not a big fan of using musical symbols in the design, treble clefs, eighth notes, etc.) But something classy. I'm uploading unformatted copy, and two logos: one of the radio station that is helping to sponsor the event, and one for the organization the concert is benefitting. This is quick turnaround, so I promise to be very responsive with feedback. Thanks!

```html
<!DOCTYPE html>
<html lang="en">
<head>
<meta charset="utf-8">
<title>Lantern Jubilee – Live Music On Concert</title>
<link rel="stylesheet" href="https://fonts.googleapis.com/css2?family=Open+Sans:wdth,wght@75..100,300..800&display=swap">
<style>
  :root{
    --backdrop:#e4e3e1;
    --olive:#b3a514;
    --ink:#1c1a17;
    --red:#e01f47;
    --black-band:#141416;
    --grey-box:#c9c9c9;
    --white:#ffffff;
    --paper:#ffffff;
    --radio-blue:#5a6b86;
  }
  *{box-sizing:border-box;margin:0;padding:0}
  html,body{width:1200px;height:1148px;overflow:hidden}
  body{background:var(--backdrop);font-family:"Open Sans",Arial,sans-serif;position:relative}
  .flyer{position:absolute;left:210px;top:44px;width:780px;height:1060px;overflow:hidden;background:var(--paper);box-shadow:0 2px 10px rgba(0,0,0,.15)}
  .flyer-panels{position:absolute;inset:0;width:780px;height:1060px}
  .tilt{position:absolute;transform:rotate(-9deg);transform-origin:left top;white-space:nowrap;font-stretch:75%;line-height:1}
  .event-mark{left:128px;top:40px;color:var(--red);font-weight:800;font-size:21px;text-transform:uppercase;line-height:1.05}
  .presenter{left:140px;top:112px;font-weight:700;font-size:16px;color:var(--ink);letter-spacing:.5px}
  .headline{color:var(--ink);font-weight:700;text-transform:uppercase}
  .headline-live{left:150px;top:130px;font-size:120px}
  .headline-music{left:165px;top:250px;font-size:96px}
  .headline-concert{left:74px;top:362px;font-size:68px}
  .tagline{left:70px;top:462px;font-size:21px;color:var(--ink);font-weight:400;line-height:1.1}
  .tagline strong{display:block;color:var(--red);font-weight:700;padding-left:48px}
  .dates{left:338px;top:396px;color:var(--ink);text-align:center}
  .dates-range{font-size:22px;font-weight:500}
  .dates-month{font-size:18px;font-weight:500}
  .dates-year{font-size:34px;font-weight:800}
  .venue{left:452px;top:334px;color:var(--white)}
  .venue-name{font-size:32px;font-weight:300;line-height:1.06;text-transform:uppercase}
  .venue-info{font-size:14px;font-weight:700;margin-top:8px;text-transform:uppercase}
  .lineup{left:380px;top:482px;color:var(--white);text-transform:uppercase}
  .lineup-label{font-size:27px;font-weight:800}
  .lineup-headliner{font-size:36px;font-weight:400;line-height:1.05;padding-left:10px}
  .lineup-rule{height:2px;background:var(--white);width:320px;margin:7px 0 7px 12px}
  .lineup-support{font-size:19px;font-weight:400;line-height:1.15;padding-left:24px}
  .sponsor{font-weight:700}
  .sponsor-radio{left:470px;top:712px;font-size:26px;color:var(--radio-blue)}
  .sponsor-radio small{display:block;font-size:12px;margin-top:4px;line-height:1.2}
  .sponsor-care{left:652px;top:660px;font-size:17px;color:var(--ink);text-align:center;line-height:1.1}
  .sponsor-care .badge{display:block;width:32px;height:32px;background:var(--ink);margin:0 auto 6px}
</style>
</head>
<body>
<main class="flyer">
  <svg class="flyer-panels" viewBox="0 0 780 1060" xmlns="http://www.w3.org/2000/svg">
    <defs>
      <linearGradient id="guitarist-tones" x1="0" y1="0" x2="1" y2="1">
        <stop offset="0" stop-color="#2f3f4f"/>
        <stop offset=".5" stop-color="#a98455"/>
        <stop offset="1" stop-color="#1d2a36"/>
      </linearGradient>
      <linearGradient id="stage-tones" x1="0" y1="0" x2="1" y2="1">
        <stop offset="0" stop-color="#d8d8d8"/>
        <stop offset=".5" stop-color="#6c6c6c"/>
        <stop offset="1" stop-color="#1e1e1e"/>
      </linearGradient>
      <linearGradient id="crowd-tones" x1="0" y1="0" x2="0" y2="1">
        <stop offset="0" stop-color="#4e6b7a"/>
        <stop offset=".55" stop-color="#8fb0bd"/>
        <stop offset="1" stop-color="#0c0f14"/>
      </linearGradient>
    </defs>
    <g role="img" aria-label="Photo of a guitarist in a leather jacket playing an acoustic guitar">
      <polygon points="300,0 780,0 780,262 430,318" fill="url(#guitarist-tones)"/>
    </g>
    <g role="img" aria-label="Black and white photo of a guitarist on a smoky stage with a drum kit">
      <polygon points="0,530 330,478 362,473 398,665 470,840 0,940" fill="url(#stage-tones)"/>
    </g>
    <g role="img" aria-label="Photo of a concert crowd with raised hands under stage lights">
      <polygon points="0,940 470,840 780,790 780,1060 0,1060" fill="url(#crowd-tones)"/>
    </g>
    <polygon class="panel-olive" points="0,0 300,0 430,318 440,370 326,388 330,478 0,530" fill="var(--olive)"/>
    <polygon class="panel-venue" points="430,318 780,262 780,407 442,460" fill="var(--black-band)"/>
    <polygon class="panel-date" points="326,388 440,370 442,460 330,478" fill="var(--grey-box)"/>
    <polygon class="panel-lineup" points="362,473 442,460 780,407 780,602 398,665" fill="var(--red)"/>
    <polygon class="panel-partners" points="398,665 780,602 780,790 470,840" fill="var(--white)"/>
  </svg>

  <p class="tilt event-mark">Midwinter<br>Lantern Jubilee</p>
  <p class="tilt presenter">LOREL IPSUM PRESENTS</p>
  <h1>
    <span class="tilt headline headline-live">Live</span>
    <span class="tilt headline headline-music">Music</span>
    <span class="tilt headline headline-concert">On Concert</span>
  </h1>
  <p class="tilt tagline">The Greats Event Music<strong>Live Performance</strong></p>

  <div class="tilt dates">
    <div class="dates-range">06-08</div>
    <div class="dates-month">JANUARY</div>
    <div class="dates-year">2018</div>
  </div>

  <div class="tilt venue">
    <div class="venue-name">The Marigold<br>Night Club</div>
    <div class="venue-info">Door open at 9PM| $5 ticket entry</div>
  </div>

  <div class="tilt lineup">
    <div class="lineup-label">Featuring Performance</div>
    <div class="lineup-headliner">The Corwin Vale</div>
    <div class="lineup-rule"></div>
    <div class="lineup-support">The Dellan // Rosa Fenwick<br>Tobias Lorne<br>And other</div>
  </div>

  <div class="tilt sponsor sponsor-radio">88.3 KVLR<small>CLASSICAL PUBLIC RADIO<br>kvlr.org</small></div>
  <div class="tilt sponsor sponsor-care"><span class="badge"></span>Riverbend Care<br>for the Unhoused</div>
</main>
</body>
</html>
```